Coffee Bag Label

I need a coffee bag label designed (front label and back label):
Our company "Mora-Vale" imports organic coffee beans direct from a farm on Vorsela Mountain on a private reserve (rainforest) from Jinotega, Nicaragua.
Labels should each be 3 inches x 3 inches (with room on edges for bleed). I want the front label to catch the eye and coordinate well with the coffee bag. The bags sizes are below and pictures are attached.
Bag sizes: Lime green 12 oz bag: 3-3/8" x 2-9/16" x 10-1/4"
Black 2 oz sample stand up pouch: 4" x 6-1/2" + 2-3/8", 2oz (60g)
Black 2lb bag: 5" x 3-3/8" x 15", 2lb (1kg)
Please include as much as possible below on the front label without it looking too wordy:
1) Our logo (it's attached). Feel free to do something creative with just the bean and place "Mora-Vale" or "Tidy-Pod Coffees" somewhere else. They don't have to be together like in the attached file. The bean can be in the background of the label as well or something else cool like in the form of a cloud over the volcano or as the sun in the sky over the volcano.
2) lime green, burnt orange, dark brown & black
3) Front label should say:
"100% Premium Arabica Nicaraguan Coffee"
"Organic, Rain Forest & Mountain Shade Grown"
Bottom of label:
"Medium Roast"
"Full body, bold flavor, nutty, hints of chocolate, with a distinct & flavorful aroma."
I want one front label file for each size bag: "2 oz" "12 oz" & "32 oz"
Back of the label:
I have uploaded a hand drawn pic of what I am thinking but if you have a better idea please submit it.
Please include as much as possible below without it looking wordy:
Directions on the perfect cup:
***2 Tbsp high quality coffee 6 Oz. cup of pure filtered water
(these can be tied into the hand-drawn picture. I will label the section each one corresponds to)
Organically Grown (sustainable)
Rainforest Grown (sustainable)
Mountain Shade Grown (sustainable)
Hand Picked (select)
Spring Water Washed (select)
Sun Dried (select)
Social Responsibility (profits help fund Bright Path Outreach Nicaragua www.brightpathoutreach.example.org)
Single Source Coffee (Single source)
Traceable Source (single source)
Website: www.Tidy-Pod.example.com
Reason: I have been asked to extend deadline by a few designers.
Thanks,
Joanne Pelter
ages 18-54
- Should have a cool border. Maybe fade from one color to another or have something more original than just a 3x3 square border.

```html
<!DOCTYPE html>
<html lang="en">
<head>
<meta charset="utf-8">
<title>Mora-Vale Organic Coffee – 12 oz Front Label</title>
<link rel="stylesheet" href="https://fonts.googleapis.com/css2?family=Oswald:wght@300&family=Tinos:wght@700&family=Arimo:wght@400&display=swap">
<style>
  :root {
    --frame-dark: #24160d;
    --frame-green: #7a8a3a;
    --frame-orange: #e39a3c;
    --bean-brown: #5a3320;
    --sack-tan: #c9a067;
    --ink-dark: #2a170d;
    --mark-red: #6e2416;
    --burnt-orange: #f07f1e;
    --band-orange: #f7a13c;
    --text-black: #161310;
  }
  * { margin: 0; padding: 0; box-sizing: border-box; }
  html, body {
    width: 1199px;
    height: 1200px;
    overflow: hidden;
    background: #ffffff;
  }
  .label {
    position: relative;
    width: 1199px;
    height: 1200px;
    background: linear-gradient(135deg, var(--frame-green) 0%, var(--frame-dark) 35%, var(--frame-dark) 70%, var(--frame-orange) 100%);
  }
  .label-photo {
    position: absolute;
    left: 24px;
    top: 24px;
    width: 1151px;
    height: 1151px;
    background:
      radial-gradient(ellipse 55% 45% at 85% 10%, rgba(232, 185, 100, 0.9), transparent 70%),
      radial-gradient(ellipse 50% 50% at 90% 70%, rgba(217, 210, 122, 0.75), transparent 70%),
      radial-gradient(ellipse 45% 35% at 20% 90%, rgba(201, 160, 103, 0.95), transparent 70%),
      radial-gradient(ellipse 40% 30% at 10% 10%, rgba(160, 120, 80, 0.9), transparent 70%),
      linear-gradient(160deg, #8a5a36 0%, var(--bean-brown) 45%, #7a5a38 75%, var(--sack-tan) 100%);
  }
  .brand-mark {
    position: absolute;
    left: 455px;
    top: 150px;
    width: 205px;
    height: 205px;
    border-radius: 50%;
    background: var(--mark-red);
  }
  .brand-name {
    position: absolute;
    left: 0;
    top: 358px;
    width: 100%;
    text-align: center;
    font-family: "Oswald", sans-serif;
    font-weight: 300;
    font-size: 236px;
    line-height: 1;
    color: var(--ink-dark);
  }
  .brand-tagline {
    position: absolute;
    left: 0;
    top: 640px;
    width: 100%;
    text-align: center;
    font-family: "Oswald", sans-serif;
    font-weight: 300;
    font-size: 38px;
    letter-spacing: 0.5em;
    text-indent: 0.5em;
    color: var(--mark-red);
  }
  .claim {
    position: absolute;
    left: 0;
    width: 100%;
    text-align: center;
    font-family: "Tinos", serif;
    font-weight: 700;
    font-size: 48px;
    line-height: 1;
    color: var(--burnt-orange);
    white-space: nowrap;
  }
  .claim--origin { top: 764px; }
  .claim--growing { top: 843px; }
  .roast-level {
    position: absolute;
    right: 49px;
    top: 986px;
    font-family: "Arimo", sans-serif;
    font-size: 33px;
    color: var(--text-black);
  }
  .tasting-band {
    position: absolute;
    left: 24px;
    top: 1050px;
    width: 1151px;
    height: 109px;
    background: var(--band-orange);
  }
  .tasting-notes {
    position: absolute;
    left: 0;
    top: 12px;
    width: 100%;
    text-align: center;
    font-family: "Arimo", sans-serif;
    font-size: 30px;
    color: var(--text-black);
    white-space: nowrap;
  }
  .net-weight {
    position: absolute;
    right: 27px;
    top: 52px;
    font-family: "Arimo", sans-serif;
    font-size: 33px;
    color: var(--text-black);
  }
</style>
</head>
<body>
  <main class="label">
    <div class="label-photo" role="img" aria-label="Photograph of roasted coffee beans spilling from an open burlap sack in warm light"></div>

    <div class="brand-mark" aria-hidden="true"></div>
    <h1 class="brand-name">Mora-Vale</h1>
    <p class="brand-tagline">ORGANIC COFFEE</p>

    <p class="claim claim--origin">100% Premium Arabica Nicaraguan Coffee</p>
    <p class="claim claim--growing">Organic, Rain Forest &amp; Mountain Shade Grown</p>

    <p class="roast-level">Medium Roast</p>

    <section class="tasting-band">
      <p class="tasting-notes">Full body, bold flavor, nutty, hints of chocolate, with a distinct &amp;&nbsp; flavorful aroma.</p>
      <p class="net-weight">12 oz</p>
    </section>
  </main>
</body>
</html>
```